Brindle Works PPT design

We are looking for a fresh and funky PPT design that is both eye-catching and allows room/whitespace for us to get the content across. We are a social media agency based in China and our logo although simple sort of reflects the nature of the company. There are two main tasks for this PPT, one as a business card to show-case our case-studies, but also as a back-drop to our pitch presentations and other client presentations. These presentations are a mix of visuals, text and graphs. The key message we want to get across is that we are professional, creative and fresh. We think that using our four support colours may work but are open to suggestions.
Current website www.brindleworks-demo.com
Reason: Hi All,
as we have just guaranteed the payment we extended the deadline to allow for more submissions. Please bear with us.
Thanks,
Brindle Works Team
Reason: To see more designs, we extend the deadline to March 18, 2014. Thanks.
Target Market(s)
Marketing CMO's, company CEO's, product managers, social media managers
Industry/Entity Type
Business
Look and feel

```html
<!DOCTYPE html>
<html lang="en">
<head>
<meta charset="utf-8">
<title>Brindle Works – Content Slide</title>
<link href="https://fonts.googleapis.com/css2?family=Arimo:wght@400;700&display=swap" rel="stylesheet">
<style>
  :root {
    --stage: #000000;
    --slide-bg: #f0f0f0;
    --footer-bg: #464751;
    --title-green: #6ad43f;
    --subtitle-grey: #5b5b66;
    --body-text: #24242c;
    --bullet-purple: #8c3fa6;
    --footer-text: #ffffff;
  }
  * { margin: 0; padding: 0; box-sizing: border-box; }
  html, body {
    width: 1200px;
    height: 1000px;
    overflow: hidden;
    background: var(--stage);
    font-family: "Arimo", Arial, sans-serif;
  }
  .slide {
    position: absolute;
    left: 29px;
    top: 72px;
    width: 1141px;
    height: 856px;
    background: var(--slide-bg);
  }
  .slide-title {
    position: absolute;
    left: 68px;
    top: 66px;
    font-size: 41px;
    font-weight: 700;
    color: var(--title-green);
    letter-spacing: 0.2px;
    line-height: 48px;
  }
  .slide-subtitle {
    position: absolute;
    left: 68px;
    top: 121px;
    font-size: 22px;
    color: var(--subtitle-grey);
    line-height: 26px;
  }
  .bullet-list {
    position: absolute;
    left: 0;
    top: 340px;
    list-style: none;
  }
  .bullet-list li {
    position: absolute;
    white-space: nowrap;
    font-size: 29px;
    line-height: 34px;
    color: var(--body-text);
  }
  .bullet-list .marker {
    position: absolute;
    color: var(--bullet-purple);
  }
  .level-1 { left: 110px; top: 0; }
  .level-1 .marker { left: -42px; font-size: 24px; top: -1px; }
  .level-2 { left: 160px; }
  .level-2 .marker { left: -35px; font-size: 22px; }
  .level-2.first { top: 45px; }
  .level-2.second { top: 91px; }
  .level-3 { left: 210px; top: 136px; }
  .level-3 .marker { left: -26px; font-size: 20px; }
  .level-4 { left: 267px; top: 182px; }
  .level-4 .marker { left: -29px; top: 4px; font-size: 14px; }
  .footer-band {
    position: absolute;
    left: 0;
    bottom: 0;
    width: 100%;
    height: 55px;
    background: var(--footer-bg);
  }
  .footer-brand {
    position: absolute;
    left: 72px;
    top: 15px;
    font-size: 22px;
    font-weight: 700;
    color: var(--footer-text);
    line-height: 26px;
  }
</style>
</head>
<body>
  <main class="slide">
    <h1 class="slide-title">LOREM IPSUM DOLOR SIT AMET</h1>
    <p class="slide-subtitle">Lorem ipsum dolor sit amet</p>

    <ul class="bullet-list">
      <li class="level-1"><span class="marker">»</span>Lorem ipsum dolor sit amet</li>
      <li class="level-2 first"><span class="marker">•</span>Lorem ipsum dolor sit amet</li>
      <li class="level-2 second"><span class="marker">•</span>Lorem ipsum dolor sit amet</li>
      <li class="level-3"><span class="marker">–</span>Lorem ipsum dolor sit amet</li>
      <li class="level-4"><span class="marker">○</span>Lorem ipsum dolor sit amet</li>
    </ul>

    <footer class="footer-band">
      <span class="footer-brand">Brindle Works</span>
    </footer>
  </main>
</body>
</html>
```